Swim school needs flyer design

Need revamp of flyer design. Attached last years flyer (BCP A4 Holiday Leaflet-v6.2 (1)). Also attached is this years information in word format (BCP A4 BCP & Holiday Leaflet 2014-2015).
This flyer must fit with our logo (Blue Current Pools-RGB). This flyer is our first point of call for many of our clients. With the amount of information that must be provided, it is important that it flows and is appealing. Photos can be accessed from http://kemapics.brightfolio.net/apps/photos/album?albumid=52930417 or from your own source
Important that the final design fits printers template.(Flyers-A4-210x297mm-2Side - attached)

```html
<!DOCTYPE html>
<html lang="en">
<head>
<meta charset="utf-8">
<title>Holiday Swim Classes – Blue Current Pools</title>
<link href="https://fonts.googleapis.com/css2?family=Arimo:wght@400;700&family=Lato:wght@400;700&display=swap" rel="stylesheet">
<style>
  :root {
    --orange: #f39200;
    --orange-deep: #e8860a;
    --green: #b7cf1e;
    --cyan: #1aa9d6;
    --band-blue: #10acd8;
    --ink: #222222;
    --paper: #ffffff;
    --paper-shade: #f2f2f2;
  }
  * { margin: 0; padding: 0; box-sizing: border-box; }
  html, body { width: 849px; height: 1200px; overflow: hidden; background: #dcdcdc; }
  .flyer {
    position: relative; width: 849px; height: 1200px; overflow: hidden;
    background: linear-gradient(180deg, var(--paper) 0%, var(--paper) 38%, var(--paper-shade) 55%, var(--paper) 80%);
    font-family: "Arimo", Arial, sans-serif; color: var(--ink);
  }
  .decor { position: absolute; left: 0; top: 0; width: 849px; height: 1200px; }
  .brand {
    position: absolute; left: 52px; top: 178px;
    display: flex; align-items: center; gap: 12px;
    font-family: "Lato", sans-serif; font-weight: 700; font-size: 38px; color: var(--cyan);
  }
  .brand-dot { width: 22px; height: 22px; border-radius: 50%; background: var(--cyan); }
  .contact { position: absolute; right: 38px; top: 52px; text-align: right; }
  .contact-web { font-family: "Lato", sans-serif; font-size: 21px; color: var(--orange); letter-spacing: .3px; }
  .contact-phone { font-family: "Arimo", sans-serif; font-size: 60px; color: var(--cyan); line-height: 1.05; margin-top: 6px; letter-spacing: 1px; }
  .venue { margin-top: 10px; font-size: 12px; line-height: 1.25; }
  .venue-name { font-weight: 700; font-size: 13px; }
  .title-band {
    position: absolute; left: 38px; right: 0; top: 258px; height: 110px;
    background: var(--band-blue); border-radius: 0 0 0 0;
    display: flex; align-items: center; justify-content: center;
  }
  .title-band h1 {
    font-family: "Arimo", sans-serif; font-weight: 700; font-size: 62px; color: #fff;
    text-shadow: 2px 3px 3px rgba(0,0,0,.45); letter-spacing: .5px;
  }
  .side-tab { position: absolute; background: var(--orange); }
  .photo {
    position: absolute; top: 406px; width: 208px; height: 208px; border-radius: 50%;
    border: 6px solid var(--green); box-shadow: inset 0 0 0 6px var(--cyan);
  }
  .photo-1 { left: 49px;  background: radial-gradient(circle at 50% 45%, #f2c7c9 0%, #9fd3df 55%, #4fb4cf 100%); }
  .photo-2 { left: 322px; background: radial-gradient(circle at 50% 45%, #efc4a9 0%, #b07aa6 45%, #3aa5c6 100%); }
  .photo-3 { left: 578px; background: radial-gradient(circle at 50% 50%, #f1cdd0 0%, #c9b0c3 45%, #6ec0d6 100%); }
  .dates-heading {
    position: absolute; left: 0; right: 0; top: 645px; text-align: center;
    font-weight: 700; font-size: 37px; color: var(--orange-deep);
  }
  .schedule {
    position: absolute; left: 162px; top: 698px; width: 522px;
    border-collapse: collapse; font-size: 24px;
  }
  .schedule td { height: 41.75px; border: 1px solid var(--orange-deep); padding-left: 52px; }
  .schedule .year {
    width: 156px; padding: 0; text-align: center; background: var(--orange-deep);
    color: #fff; font-weight: 700; font-size: 30px;
  }
  .schedule tr:nth-child(odd) .week { background: var(--orange-deep); }
  .schedule tr:nth-child(even) .week { background: #fff; }
  .price-note { position: absolute; left: 0; right: 0; top: 1038px; text-align: center; font-size: 19px; }
  .tagline {
    position: absolute; left: 0; right: 0; top: 1092px; text-align: center;
    font-family: "Lato", sans-serif; font-size: 18px; line-height: 1.3;
  }
</style>
</head>
<body>
<main class="flyer">
  <svg class="decor" viewBox="0 0 849 1200" aria-hidden="true">
    <rect x="0" y="0" width="420" height="28" fill="var(--green)"/>
    <rect x="420" y="0" width="429" height="28" fill="var(--orange)"/>
    <path d="M0 230 C 160 200, 300 250, 420 290 L 0 290 Z" fill="var(--orange)"/>
    <path d="M0 246 C 160 222, 300 262, 420 298 L 0 298 Z" fill="#fff"/>
    <path d="M849 120 C 820 210, 720 280, 560 290 L 849 290 Z" fill="var(--green)"/>
    <path d="M849 150 C 815 230, 720 284, 580 292 L 849 292 Z" fill="#fff" opacity="0"/>
    <path d="M0 1090 C 120 1050, 260 1055, 360 1085 L 0 1085 Z" fill="var(--green)"/>
    <path d="M849 1090 C 720 1050, 580 1055, 490 1085 L 849 1085 Z" fill="var(--green)"/>
    <path d="M0 1095 C 120 1062, 260 1064, 360 1090 L 0 1090 Z" fill="var(--orange)" opacity=".0"/>
    <rect x="0" y="1176" width="420" height="24" fill="var(--orange)"/>
    <rect x="420" y="1176" width="429" height="24" fill="var(--green)"/>
  </svg>

  <header>
    <div class="brand"><span class="brand-dot"></span>Blue Current Pools</div>
    <div class="contact">
      <p class="contact-web">www.bluecurrentpools.com.au</p>
      <p class="contact-phone">9387 2640</p>
      <p class="venue"><span class="venue-name">Ridgeview P.S. Pool</span><br>42 Banksia Street Ridgeview</p>
      <p class="venue"><span class="venue-name">Elmwood Grammar Pool</span><br>Gate 1, Marlow St Elmwood</p>
    </div>
  </header>

  <section class="title-band"><h1>Holiday Swim Classes</h1></section>

  <div class="side-tab" style="left:0;top:452px;width:40px;height:92px"></div>
  <div class="side-tab" style="right:0;top:452px;width:40px;height:92px"></div>

  <div class="photo photo-1" role="img" aria-label="Photo of a child swimming underwater in pink goggles"></div>
  <div class="photo photo-2" role="img" aria-label="Photo of a child in a swim cap and goggles in the pool"></div>
  <div class="photo photo-3" role="img" aria-label="Photo of a child gliding underwater with arms raised"></div>

  <h2 class="dates-heading">Holiday Program Dates</h2>

  <div class="side-tab" style="left:0;top:808px;width:156px;height:102px"></div>
  <div class="side-tab" style="right:0;top:808px;width:160px;height:102px"></div>

  <table class="schedule">
    <tr><td class="year" rowspan="2">2014</td><td class="week">Sep 23rd – 27th</td></tr>
    <tr><td class="week">Sep 30th – Oct 4th</td></tr>
    <tr><td class="year" rowspan="6">2015</td><td class="week">Jan 6th – 10th</td></tr>
    <tr><td class="week">Jan 13th – 17th</td></tr>
    <tr><td class="week">Jan&nbsp; 20th – 24th</td></tr>
    <tr><td class="week">Mar 30th – Apr 3rd</td></tr>
    <tr><td class="week">Apr 6th&nbsp; – 10th</td></tr>
    <tr><td class="week">Jun 29th – Jul 3rd</td></tr>
  </table>

  <p class="price-note">* $52 per child due to 4 day week</p>

  <p class="tagline">Our qualified staff makes learn to swim not only a rewarding but also a lot of fun.<br>This is a great opportunity to kick-start your child’s aquatic education.</p>
</main>
</body>
</html>
```